Vyntra Ad Design for Culinary Toursim Company

Looking for ad design for www.savorlanewalks.example to be used on VYNTRA traffic ads.

Below is one example of the

We are looking for vyntra ad design
Post: 1080x1080 with text,
Stories: 1080x1920 with text

Text should read
Food For Thought
CTA: Join our {CITY} Food Tour

Logo and optional photos are attached. You can edit the photos as you see fit.
Brand guidelines https://www.filevault.example/s/k3m9q2x7/Savor-Lane-Walks-Brand-Guidelines.docx

Logos https://www.filevault.example/f/r8t4w1z6/logos

Target Market(s)

United States Foodies ages 30-65

Industry/Entity Type

Tourism

Font styles to use
Other font styles liked:
• Avenir

Requirements
Must have
• High Design
Nice to have
• See Brand Guidelines
Should not have
• See Brand Guidelines

```html
<!DOCTYPE html>
<html lang="en">
<head>
<meta charset="utf-8">
<title>Savor Lane Walks – Food For Thought</title>
<link rel="stylesheet" href="https://fonts.googleapis.com/css2?family=Figtree:wght@400;600;700;800&display=swap">
<style>
  :root {
    --brand-red: #a80303;
    --ring-red: #b30d0d;
    --deep-red: #6e0000;
    --button-red: #aa0000;
    --ink-light: #f4f1f0;
    --ink-dark: #222222;
    --backdrop-light: #eef0ec;
    --backdrop-mid: #d9ddd6;
  }
  * { margin: 0; padding: 0; box-sizing: border-box; }
  html, body {
    width: 1200px;
    height: 1200px;
    overflow: hidden;
    background: var(--backdrop-light);
  }
  .ad-canvas {
    position: relative;
    width: 1200px;
    height: 1200px;
    overflow: hidden;
    font-family: "Figtree", "Helvetica Neue", Arial, sans-serif;
  }
  .backdrop-photo {
    position: absolute;
    inset: 0;
    background:
      radial-gradient(ellipse at 20% 30%, #dfe3db 0%, transparent 55%),
      radial-gradient(ellipse at 80% 85%, #e3e6e0 0%, transparent 50%),
      linear-gradient(160deg, var(--backdrop-light) 0%, var(--backdrop-mid) 55%, var(--backdrop-light) 100%);
  }
  .circle-art {
    position: absolute;
    inset: 0;
    width: 1200px;
    height: 1200px;
  }
  .brand-mark {
    position: absolute;
    top: 70px;
    right: 40px;
    display: flex;
    align-items: center;
    gap: 12px;
  }
  .brand-mark__dot {
    width: 30px;
    height: 30px;
    border-radius: 50%;
    background: var(--brand-red);
  }
  .brand-mark__name {
    font-size: 32px;
    font-weight: 700;
    color: var(--ink-dark);
    letter-spacing: -0.3px;
  }
  .message {
    position: absolute;
    left: 0;
    width: 1200px;
    text-align: center;
    color: var(--ink-light);
  }
  .message__kicker {
    top: 312px;
    font-size: 28px;
    font-weight: 700;
  }
  .message__headline {
    top: 375px;
    font-size: 84px;
    font-weight: 800;
    line-height: 115px;
    letter-spacing: -0.5px;
  }
  .cta-button {
    position: absolute;
    left: 350px;
    top: 739px;
    width: 500px;
    height: 100px;
    border-radius: 50px;
    background: var(--button-red);
    color: var(--ink-light);
    display: flex;
    align-items: center;
    justify-content: center;
    font-size: 23px;
    font-weight: 700;
  }
  .message__url {
    top: 877px;
    font-size: 22px;
    font-weight: 400;
  }
</style>
</head>
<body>
<main class="ad-canvas">
  <div class="backdrop-photo" role="img" aria-label="Soft, faded photo of tall agave plants and greenery"></div>

  <svg class="circle-art" viewBox="0 0 1200 1200" aria-hidden="true">
    <defs>
      <radialGradient id="inner-photo-tint" cx="50%" cy="45%" r="60%">
        <stop offset="0%" stop-color="#8e0a0a"/>
        <stop offset="70%" stop-color="#730202"/>
        <stop offset="100%" stop-color="#5e0000"/>
      </radialGradient>
    </defs>
    <circle cx="597" cy="600" r="476" fill="var(--ring-red)"/>
    <circle cx="597" cy="600" r="430" fill="url(#inner-photo-tint)" role="img" aria-label="Red-tinted photo of a market vendor among agave plants"/>
    <circle cx="168" cy="1029" r="23" fill="var(--brand-red)"/>
  </svg>

  <div class="brand-mark">
    <span class="brand-mark__dot"></span>
    <span class="brand-mark__name">Savor Lane Walks</span>
  </div>

  <p class="message message__kicker">Food For Thought</p>
  <h1 class="message message__headline">Discover the<br>world's culinary<br>capitals</h1>
  <div class="cta-button">Join Our Mexico City Food Tour</div>
  <p class="message message__url">savorlanewalks.example</p>
</main>
</body>
</html>
```